Business Card Design Project

Corvexa logo will be provided after
Front

Bram Oskarsen- Construction Manager

Ph: (61) 07 53182907
boskarsen@corvexa.com.au
PO Box 83 Kelbarra 4529

Back
Corvexa
EPCM

Oil - Gas - Mining

Industry/Entity Type

Business

Font styles to use
Sans Serif

Colors
faa54b

Requirements
Must have
• White Back Ground

```html
<!DOCTYPE html>
<html lang="en">
<head>
<meta charset="utf-8">
<title>Corvexa Business Card</title>
<link rel="stylesheet" href="https://fonts.googleapis.com/css2?family=Open+Sans:wght@400;600;700;800&display=swap">
<style>
  :root {
    --page-bg: #e9e7e3;
    --card-white: #ffffff;
    --ink-black: #161616;
    --ink-dark: #2e2e2e;
    --accent: #faa54b;
    --accent-deep: #f29a1f;
    --grey-text: #8d8d8d;
    --grey-light: #c9c9c9;
    --band-grey: #dcdcdc;
  }
  * { box-sizing: border-box; margin: 0; padding: 0; }
  html, body {
    width: 1200px; height: 1023px; overflow: hidden;
    background: var(--page-bg);
    font-family: "Open Sans", Arial, sans-serif;
  }
  .canvas { position: relative; width: 1200px; height: 1023px; }
  .card {
    position: absolute; left: 320px; width: 560px; height: 320px;
    border-radius: 20px; overflow: hidden; background: var(--card-white);
    box-shadow: 0 10px 28px rgba(0,0,0,0.18);
  }
  .card--front { top: 90px; }
  .card--back { top: 600px; }

  .front-art { position: absolute; inset: 0; }
  .front-brand {
    position: absolute; left: 34px; top: 92px;
    font-size: 40px; font-weight: 800; letter-spacing: 2px;
    color: var(--grey-light); text-transform: uppercase;
  }
  .front-name {
    position: absolute; left: 36px; top: 170px;
    font-size: 24px; font-weight: 400; letter-spacing: 1px;
    color: var(--accent); text-transform: uppercase;
  }
  .front-title {
    position: absolute; left: 37px; top: 204px;
    font-size: 13px; letter-spacing: 1.5px;
    color: var(--grey-text); text-transform: uppercase;
  }
  .contact-list {
    position: absolute; right: 22px; top: 176px; list-style: none;
    text-align: right;
  }
  .contact-item {
    display: flex; align-items: center; justify-content: flex-end; gap: 8px;
    font-size: 12.5px; color: #6a6a6a; margin-bottom: 9px;
    white-space: nowrap;
  }
  .contact-icon {
    width: 16px; height: 16px; border-radius: 3px; background: var(--accent);
    display: inline-flex; align-items: center; justify-content: center;
    flex: none;
  }
  .address-band {
    position: absolute; right: 0; bottom: 0; width: 250px; height: 48px;
    background: linear-gradient(180deg, #ececec, var(--band-grey));
    display: flex; align-items: center; justify-content: flex-end; padding-right: 22px;
  }
  .address-text {
    font-size: 14px; font-weight: 700; letter-spacing: 0.5px;
    color: var(--accent-deep); text-transform: uppercase; white-space: nowrap;
  }

  .back-brand {
    position: absolute; left: 0; right: 0; top: 110px; text-align: center;
    font-size: 58px; font-weight: 800; letter-spacing: 4px;
    color: var(--ink-black); text-transform: uppercase;
  }
  .sector-line {
    position: absolute; left: 44px; top: 36px;
    font-size: 14px; font-weight: 600; letter-spacing: 2px;
    color: #5a5a5a; text-transform: uppercase;
    display: flex; align-items: center; gap: 10px;
  }
  .sector-dot { width: 7px; height: 7px; border-radius: 50%; background: var(--accent); }
</style>
</head>
<body>
<main class="canvas">
  <section class="card card--front" aria-label="Card front">
    <svg class="front-art" width="560" height="320" viewBox="0 0 560 320" aria-hidden="true">
      <defs>
        <linearGradient id="panelShade" x1="0" y1="0" x2="1" y2="1">
          <stop offset="0" stop-color="#3a3a3a"/>
          <stop offset="0.55" stop-color="#1c1c1c"/>
          <stop offset="1" stop-color="#0c0c0c"/>
        </linearGradient>
        <linearGradient id="accentShade" x1="0" y1="0" x2="0" y2="1">
          <stop offset="0" stop-color="#fbb65e"/>
          <stop offset="1" stop-color="#f29a1f"/>
        </linearGradient>
      </defs>
      <path d="M0 0 H258 Q358 160 300 320 H0 Z" fill="url(#accentShade)"/>
      <path d="M0 0 H240 Q338 160 280 320 H0 Z" fill="url(#panelShade)"/>
    </svg>
    <div class="front-brand">Corvexa</div>
    <div class="front-name">Bram Oskarsen</div>
    <div class="front-title">Construction Manager</div>
    <ul class="contact-list">
      <li class="contact-item">(61) 07 53182907
        <span class="contact-icon"><svg width="10" height="10" viewBox="0 0 10 10"><path d="M2 1 L4 1 L4.6 3 L3.5 4 Q4.5 6 6 6.5 L7 5.4 L9 6 L9 8 Q5 9 2 5.5 Q1 3.5 2 1Z" fill="#fff"/></svg></span>
      </li>
      <li class="contact-item">boskarsen@corvexa.com.au
        <span class="contact-icon"><svg width="10" height="10" viewBox="0 0 10 10"><rect x="1" y="2.5" width="8" height="5.5" fill="none" stroke="#fff" stroke-width="1"/><path d="M1 2.5 L5 6 L9 2.5" fill="none" stroke="#fff" stroke-width="1"/></svg></span>
      </li>
    </ul>
    <div class="address-band"><span class="address-text">PO Box 83 Kelbarra 4529</span></div>
  </section>

  <section class="card card--back" aria-label="Card back">
    <div class="sector-line">
      <span>Oil</span><span class="sector-dot"></span><span>Gas</span><span class="sector-dot"></span><span>Mining</span>
    </div>
    <div class="back-brand">Corvexa</div>
  </section>
</main>
</body>
</html>
```